Business card design for Larkspire Bullion

I am looking for business card design concepts for my company, Larkspire Bullion. Please visit the website for more information www.larkspirebullion.example
I would like to use the logo you will see on the website.
I want a modern design that reflects the multi-thousand year history of precious metals use in the global economy. This is a very important subject that everyone needs to understand. I want the card to be classy and professional reflecting my personal commitment to the concept!

Target Market(s)

Individuals with funds to invest in precious metals.....gold,silver,etc.

Industry/Entity Type

Financial Service

Contact Information for Business Card

Should reflect the commitment to precious metals for everyone!

Font styles to use
Sans Serif

Colors
3276b5
0255a3

Requirements
Must have
• Logo, name: Tobias Renn, title: Owner, email address:tobias@larkspirebullion.example
• Phone numbers: Toll free 1-800-914-2057, local: 503-712-4193
• Website address: www.larkspirebullion.example, address: 2780 Quarry Lane SE, Portland, OR 97231
• Larger lettering for ease of reading (use both sides)
• "Trusted Metals Guidance for Every Investor" somewhere on the card!
Nice to have
• The color blue that matches the website blue.....
Should not have
• No black cards please.

```html
<!DOCTYPE html>
<html lang="en">
<head>
<meta charset="utf-8">
<title>Larkspire Bullion — Business Card</title>
<link rel="stylesheet" href="https://fonts.googleapis.com/css2?family=Lato:wght@400;700;900&display=swap">
<style>
  :root {
    --blue-deep: #0255a3;
    --blue-light: #3276b5;
    --gold: #e0a23f;
    --paper: #f6f6f6;
    --ink: #222222;
    --backdrop: #e4e6ea;
    --white: #ffffff;
  }
  * { margin: 0; padding: 0; box-sizing: border-box; }
  html, body { width: 1200px; height: 997px; overflow: hidden; }
  body {
    background: var(--backdrop);
    font-family: "Lato", sans-serif;
    position: relative;
  }
  .card {
    position: absolute;
    width: 560px;
    height: 320px;
    box-shadow: 0 10px 30px rgba(0,0,0,0.18);
    overflow: hidden;
  }
  /* Front */
  .card-front {
    left: 70px; top: 110px;
    background: linear-gradient(135deg, var(--blue-light), var(--blue-deep));
    display: flex; flex-direction: column; align-items: center; justify-content: center;
    gap: 18px;
  }
  .brand-mark { width: 70px; height: 70px; background: var(--gold); }
  .brand-name {
    font-weight: 900; font-size: 44px; color: var(--gold);
    letter-spacing: 2px; text-transform: uppercase;
  }
  .tagline { font-size: 12px; color: var(--white); letter-spacing: 2px; }
  /* Back */
  .card-back { left: 570px; top: 520px; background: var(--paper); }
  .back-shape { position: absolute; left: 0; top: 0; }
  .back-brand {
    position: absolute; left: 0; right: 0; top: 44px; text-align: center;
    font-weight: 900; font-size: 34px; color: var(--gold);
    letter-spacing: 2px; text-transform: uppercase;
  }
  .person { position: absolute; right: 40px; top: 110px; text-align: right; }
  .person-name { font-weight: 700; font-size: 18px; color: var(--blue-deep); }
  .person-title { font-size: 12px; color: var(--ink); margin-top: 2px; }
  .contact-list { position: absolute; left: 28px; top: 150px; list-style: none; }
  .contact-item {
    display: flex; align-items: center; gap: 10px;
    font-size: 14px; color: var(--ink); margin-bottom: 8px;
  }
  .contact-icon {
    width: 20px; height: 20px; border-radius: 50%;
    background: var(--blue-deep);
    display: flex; align-items: center; justify-content: center;
  }
  .address {
    position: absolute; left: 28px; top: 246px;
    font-weight: 700; font-size: 14px; color: var(--blue-deep);
  }
  .website {
    position: absolute; right: 24px; bottom: 16px;
    font-weight: 700; font-size: 14px; color: var(--white);
  }
</style>
</head>
<body>

<section class="card card-front">
  <div class="brand-mark"></div>
  <div class="brand-name">Larkspire Bullion</div>
  <div class="tagline">Trusted Metals Guidance for Every Investor</div>
</section>

<section class="card card-back">
  <svg class="back-shape" width="560" height="320" viewBox="0 0 560 320">
    <path d="M0 306 C 220 302, 440 252, 560 180 L560 320 L0 320 Z" fill="var(--blue-deep)"/>
    <path d="M200 300 C 350 287, 470 232, 560 162" fill="none" stroke="var(--gold)" stroke-width="7"/>
  </svg>

  <div class="back-brand">Larkspire Bullion</div>

  <div class="person">
    <div class="person-name">Tobias Renn</div>
    <div class="person-title">Owner</div>
  </div>

  <ul class="contact-list">
    <li class="contact-item">
      <span class="contact-icon">
        <svg width="12" height="12" viewBox="0 0 24 24"><path fill="#fff" d="M6.6 10.8a15 15 0 0 0 6.6 6.6l2.2-2.2a1 1 0 0 1 1-.25 11.4 11.4 0 0 0 3.6.57 1 1 0 0 1 1 1V20a1 1 0 0 1-1 1A17 17 0 0 1 3 4a1 1 0 0 1 1-1h3.5a1 1 0 0 1 1 1c0 1.25.2 2.450.57 3.6a1 1 0 0 1-.25 1z"/></svg>
      </span>503-712-4193
    </li>
    <li class="contact-item">
      <span class="contact-icon">
        <svg width="12" height="12" viewBox="0 0 24 24"><path fill="#fff" d="M6.6 10.8a15 15 0 0 0 6.6 6.6l2.2-2.2a1 1 0 0 1 1-.25 11.4 11.4 0 0 0 3.6.57 1 1 0 0 1 1 1V20a1 1 0 0 1-1 1A17 17 0 0 1 3 4a1 1 0 0 1 1-1h3.5a1 1 0 0 1 1 1c0 1.25.2 2.450.57 3.6a1 1 0 0 1-.25 1z"/></svg>
      </span>1-800-914-2057 (Toll-Free)
    </li>
    <li class="contact-item">
      <span class="contact-icon">
        <svg width="12" height="12" viewBox="0 0 24 24"><rect x="3" y="6" width="18" height="12" fill="none" stroke="#fff" stroke-width="2"/><path d="M3 6l9 7 9-7" fill="none" stroke="#fff" stroke-width="2"/></svg>
      </span>tobias@larkspirebullion.example
    </li>
  </ul>

  <div class="address">2780 Quarry Lane SE, Portland, OR 97231</div>
  <div class="website">www.larkspirebullion.example</div>
</section>

</body>
</html>
```